Marketing / Informational Site for Marriage and Family Therapists Cooperative

We need a web design for a new Marriage and Family Therapist Cooperative, called Meadowgate Counselors. This is a market and information site for potential clients and referrals to learn more about the team and get contact information.

We are looking for profession, clean, and modern design, that cater towards families and mom's concerned about their families mental health and child development.

This should include a home page, an general about page, 3 bio pages (1 for each therapist listed below), and a general contact us page.

Our Domain Name

Meadowgatecounselors.example

Company Name

Meadowgate Counselors

Group Moto/Philosophy

“Our sorrows and wounds are healed only when we touch them with compassion.” - Orvelan

Our Logo

See Heron Final (attached)

Home Page (Introduction)

Feeling stressed and overwhelmed?
Encountering barriers towards your goals?
Having difficulty accomplishing the simplest task?
Have the need to talk but unsure who to turn to?

Therapy can assist you in overcoming all of these challenges. Assist you in uncovering the difficulties and barriers that are keeping you from achieving your life’s ambitions, help discover ways to overcome them, and cope with the impact your behaviour has on your occupation, personal life and social life.

Welcome to our practice, with over 20 years of combined experience in the clinical field you are sure to find the right fit for your needs. Each clinician has experience working with groups, adults, teens, children, families, and couples. We specialize in fostering healthy relationships between individuals, managing depression and anxiety, overcoming trauma, and developing occupational success. Feel free to explore information about each clinician and make an appointment with one of us today.

About Us (bio pics attached)

Marisel Dunkworth

My name is Dr. MariSel Dunkworth and I am a Licensed Marriage Family Therapist with a practice in Riverside, CA. I have devoted my life’s work into developing my skills in this profession. I have over 15 years of experience working in the clinical and the social service settings. These years have afforded me the opportunity to work with groups, families, adults, teens and children with varying symptoms. I have helped clients that have trauma, abuse histories, and many within the legal or social service systems. I enjoy working individuals from all walks of life achieve self sufficiency, social success and occupational success. In my years of training I have come to develop a culturally sensitive practice that centers around the needs of the client.

I have held many positions in my clinical career beginning as clinician moving upwards toward supervisor and program coordinator. I have also over 5 years of experience as an adjunct faculty member in the University setting teaching student to become Marriage and Family Therapists. As a clinician I focused on enriching my clinical skills by developing outcome driven practices to achieve client’s desired goals. As a clinical supervisor, I guided clinicians along their own paths towards clinical licensure. As a program coordinator, I helped develop a clinical assessment and triage program from ground up to assist client in accessing services in the South Los Angeles Area. The program would assist over 100 plus clients on a monthly basis get connected to clinical services and linked to any additional resources as needed by the individual. I have graduated with my, Bachelor’s degree at the Halvern College, Riverside. I received my Masters degree in Clinical Psychology at Mount St. Mary’s University, and my Doctorate degree in Clinical Psychology at Tamsworth Institute.

To schedule an appointment with Dr. MariSel Dunkworth, Meadowgate:

email: marisel582@postbox.example
Phone: (951)555-0182

Jeb Kowal

My name is Rosalindra (Jeb) Kowal, I received my Masters Degree of Counseling in Marriage and Family Therapy from Corvell Bay State College in June 2000. I have acquired over 15 years of experience helping Individuals, Couples, and Families cope with issues of Anxiety, Depression, Grief and Bereavement, and HIV/AIDS.

I am a Family Systems Therapist and I truly believe the dynamics in our family of origin greatly shape our current belief systems and behaviors. However, I often utilize a variety of approaches to help my clients achieve their goals depending on their individual needs.

My greatest strength as a Marriage and Family Therapist is helping my clients explore ways to make the changes in their lives that will allow them to live their life to their fullest potential. I help my clients achieve their personal life goals with a warm, safe, non-judgmental , and supportive environment. In doing so, my clients are encouraged to explore the issues that may be preventing them from living the life they desire. Thus, empowering them to take control of their personal journey to living a productive and meaningful life.

If you feel that you are ready to commit to bringing about positive changes in your life and would like support in exploring this path, I’m here to work with you in your journey to personal growth and development.

To schedule an appointment with Rosalindra Kowal, Meadowgate:

e-mail: rkjeb7@mailnest.example
Phone: (951)555-0147

Dena Holcroft

Dena Holcroft graduated with a Masters in Marriage and Family Therapy from Pellridge Crestwood College. She currently holds a license in Marriage and Family Therapy in the State of California. She is also formally trained in Clinical Art Therapy. Dena's expertise lies in providing treatment to individuals experiencing work-related injuries, severe physical and emotional pain, trauma, grief and loss, anxiety and depression. In her early career, she provided valuable service at the largest free clinic in the nation serving marginalized families and children. For the past ten years, Dena has worked with HIV/AIDS population.
Dena comes from a multicultural background and she has utilized this experience and knowledge in serving a variety of populations. At an organizational level, Dena has worked extensively with challenging issues such as the chemical dependency and homelessness. In her private practice, Dena is proficient in working within individuals experiencing relationship concerns, marital and family conflict, depression/anxiety, self-esteem concerns, adjustment disorders, and pain management. She has treated clients from diverse cultural, linguistic backgrounds and sexual orientations.
Dena is trained in Family Systems Theory and incorporates other strategies appropriate for each presenting issue. She specializes in Clinical Art Therapy and has successfully utilized an integrated approach including guided imagery and relaxation skills training for many years.

To schedule an appointment with Dena Holcroft, Meadowgate

e-mail: greypinestudio@inkmail.example
Phone: (951) 555-0169

Target Market(s)

Families with child development, marriage issues, or other mental health needs

Industry/Entity Type

Marketing

Number of Pages Required

5+ page

Requirements
Must have
• 1 home page, 1 about page, 1 contact page. About page could either be standalone page with 3 different bio pages for each therapist or an all in one about page that includes bios for all 3 therapists.

```html
<!DOCTYPE html>
<html lang="en">
<head>
<meta charset="utf-8">
<title>Meadowgate Counselors — Marriage and Family Therapists</title>
<link href="https://fonts.googleapis.com/css2?family=Lato:wght@400;700;900&display=swap" rel="stylesheet">
<style>
:root{
  --green:#8dc63f;
  --green-dark:#6fa32a;
  --ink:#333333;
  --muted:#777777;
  --footer:#3a3a3a;
  --footer-bottom:#2a2a2a;
  --mint:#e6f3f1;
  --white:#ffffff;
  --line:#dddddd;
}
*{box-sizing:border-box;margin:0;padding:0}
html,body{width:789px;height:1200px;overflow:hidden}
body{font-family:"Lato",Arial,sans-serif;color:var(--ink);background:var(--white);position:relative}

/* header */
.site-header{position:absolute;top:0;left:0;width:789px;height:100px;background:var(--white)}
.topbar{position:absolute;top:0;right:0;width:255px;height:20px;background:var(--green)}
.social{position:absolute;top:4px;right:70px;display:flex;gap:6px}
.social span{width:12px;height:12px;background:var(--white);opacity:.85;border-radius:2px}
.brand{position:absolute;left:78px;top:18px;display:flex;align-items:center;gap:10px}
.brand-dot{width:40px;height:40px;border-radius:50%;background:var(--green)}
.brand-name{font-size:17px;font-weight:700;color:var(--green-dark);line-height:1.1;width:110px}
.contact-line{position:absolute;right:95px;top:35px;display:flex;gap:18px;font-size:11px;align-items:center}
.contact-line span{display:flex;align-items:center;gap:5px}
.nav{position:absolute;right:95px;top:64px;display:flex;font-size:11px;font-weight:700;letter-spacing:.5px}
.nav a{color:var(--ink);text-decoration:none;padding:0 10px;border-left:1px solid var(--line)}
.nav a:first-child{border-left:0}

/* hero */
.hero{position:absolute;top:100px;left:0;width:789px;height:295px;overflow:hidden}
.hero-photo{position:absolute;inset:0;background:linear-gradient(180deg,#e9eef2 0%,#c9d6c4 45%,#7d9a52 75%,#5f7f35 100%)}
.hero-caption{position:absolute;left:238px;top:163px;width:315px;background:rgba(40,40,40,.72);color:var(--white);font-weight:900;font-size:16px;line-height:1.3;text-align:center;padding:8px 10px}
.hero-wave{position:absolute;left:0;bottom:0}

/* services */
.services{position:absolute;top:408px;left:87px;width:615px;display:flex;justify-content:space-between}
.service-card{width:172px;height:184px;border:1px solid var(--line);background:var(--white);box-shadow:0 1px 3px rgba(0,0,0,.08);text-align:center;padding:14px 10px 0}
.service-icon{width:80px;height:52px;margin:0 auto 8px;border-radius:40px 40px 8px 8px;background:var(--green)}
.service-card h3{font-size:9px;font-weight:700;white-space:nowrap;margin-bottom:6px}
.service-card p{font-size:8px;line-height:1.4;color:var(--muted)}
.more{display:inline-flex;margin-top:8px;width:12px;height:12px;background:var(--green);color:var(--white);font-size:10px;font-weight:700;align-items:center;justify-content:center;line-height:1}

/* welcome */
.welcome{position:absolute;top:613px;left:0;width:789px;height:223px;background:linear-gradient(90deg,#1f1f1f,#3b3b36 60%,#2a2a28)}
.welcome h2{position:absolute;left:87px;top:10px;color:var(--white);font-size:19px;font-weight:700;letter-spacing:.5px}
.welcome-rule{position:absolute;left:87px;top:38px;width:320px;height:1px;background:rgba(255,255,255,.35)}
.portrait{position:absolute;left:87px;top:50px;width:90px;height:118px;background:linear-gradient(160deg,#a8b6a0,#6f7c68);border:3px solid var(--white)}
.welcome-text{position:absolute;left:186px;top:48px;width:225px;color:#e5e5e5;font-size:8px;line-height:1.45}
.welcome-more{position:absolute;left:87px;top:172px;width:324px;color:#e5e5e5;font-size:8px;line-height:1.45}
.slider{position:absolute;left:420px;top:20px;width:232px;height:192px;background:linear-gradient(135deg,#f2f0ee,#d9cfc6 55%,#b7a99c);border:3px solid var(--white)}
.slider-arrows{position:absolute;right:8px;bottom:8px;display:flex;gap:4px}
.slider-arrows span{width:14px;height:14px;background:var(--white);border:1px solid #999;display:flex;align-items:center;justify-content:center}

/* testimonials */
.testimonials{position:absolute;top:836px;left:0;width:789px;height:164px;background:var(--mint)}
.testimonials h2{text-align:center;color:var(--green-dark);font-size:16px;font-weight:900;margin-top:12px;letter-spacing:.5px}
.title-rule{width:60px;height:2px;background:var(--green);margin:6px auto 0}
.quotes{position:absolute;top:62px;left:87px;width:615px;display:flex;justify-content:space-between}
.quote{display:flex;align-items:flex-start;gap:10px;width:295px}
.avatar{flex:none;width:52px;height:52px;border-radius:50%;background:linear-gradient(160deg,#b7a69a,#6e5d52);border:2px solid var(--white)}
.quote-box{background:var(--white);padding:9px 10px;font-size:8.5px;line-height:1.45;color:var(--muted);font-style:italic}
.quote-box cite{display:block;margin-top:4px;font-style:normal;font-weight:700;color:var(--green-dark);font-size:8.5px}

/* footer */
.site-footer{position:absolute;top:1000px;left:0;width:789px;height:165px;background:var(--footer);color:#cfcfcf}
.footer-col{position:absolute;top:12px;width:180px}
.footer-col h4{color:var(--green);font-size:14px;font-weight:700;margin-bottom:10px;letter-spacing:.3px}
.col-contact{left:87px}.col-news{left:270px}.col-quick{left:492px}
.info-row{display:flex;gap:6px;font-size:8.5px;line-height:1.4;margin-bottom:7px}
.info-row svg{flex:none;margin-top:1px}
.footer-col p{font-size:8.5px;line-height:1.4;margin-bottom:6px}
.field{height:14px;background:#555;border:1px solid #666;color:#bbb;font-size:8px;padding:1px 5px;margin-bottom:5px;width:165px}
.field.tall{height:24px}
.btn{display:inline-block;background:var(--green);color:var(--white);font-size:8px;font-weight:700;padding:3px 8px;margin-top:2px}
.footer-bottom{position:absolute;top:1165px;left:0;width:789px;height:35px;background:var(--footer-bottom);color:#bbb;font-size:8.5px}
.footer-links{position:absolute;left:87px;top:13px}
.footer-links a{color:#bbb;text-decoration:none;padding:0 6px;border-left:1px solid #666}
.footer-links a:first-child{padding-left:0;border-left:0}
.copyright{position:absolute;right:87px;top:13px}
</style>
</head>
<body>

<header class="site-header">
  <div class="topbar"></div>
  <div class="social" aria-label="Social links"><span></span><span></span><span></span><span></span></div>
  <div class="brand"><span class="brand-dot"></span><span class="brand-name">Meadowgate Counselors</span></div>
  <div class="contact-line">
    <span><svg width="11" height="8" viewBox="0 0 11 8"><rect x=".5" y=".5" width="10" height="7" fill="none" stroke="#333"/><path d="M.5 .5l5 4 5-4" fill="none" stroke="#333"/></svg>hello@meadowgatecounselors.example</span>
    <span><svg width="9" height="9" viewBox="0 0 10 10"><path d="M2 0l2 2-1 2c1 1 2 2 3 3l2-1 2 2-2 2C4 10 0 6 0 2z" fill="#333"/></svg>+123 456 7890</span>
  </div>
  <nav class="nav"><a href="#">HOME</a><a href="#">ABOUT US</a><a href="#">CONTACT US</a></nav>
</header>

<section class="hero">
  <div class="hero-photo" role="img" aria-label="Family walking together hand in hand on a sunny lawn"></div>
  <div class="hero-caption">LOREM IPSUM DOLOR SIT AMET CONSECTETUER ADIPISCING ELIT SED DIAM NONUMMY NIBH</div>
  <svg class="hero-wave" width="789" height="40" viewBox="0 0 789 40">
    <path d="M0 40V22C200 44 520 -4 789 10V40Z" fill="#8dc63f"/>
    <path d="M0 40V30C220 48 540 8 789 22V40Z" fill="#ffffff"/>
  </svg>
</section>

<section class="services">
  <article class="service-card">
    <div class="service-icon" role="img" aria-label="Green lotus icon"></div>
    <h3>Families With Child Developments</h3>
    <p>Duis autem vel eum iriure dolor in hendrerit in vulputate velit esse molestie consequat, vel illum dolore eu</p>
    <span class="more">+</span>
  </article>
  <article class="service-card">
    <div class="service-icon" role="img" aria-label="Green lotus icon"></div>
    <h3>Marriage Issues</h3>
    <p>Duis autem vel eum iriure dolor in hendrerit in vulputate velit esse molestie consequat, vel illum dolore eu</p>
    <span class="more">+</span>
  </article>
  <article class="service-card">
    <div class="service-icon" role="img" aria-label="Green lotus icon"></div>
    <h3>Mental Health Needs</h3>
    <p>Duis autem vel eum iriure dolor in hendrerit in vulputate velit esse molestie consequat, vel illum dolore eu</p>
    <span class="more">+</span>
  </article>
</section>

<section class="welcome">
  <h2>WELCOME TO MEADOWGATE</h2>
  <div class="welcome-rule"></div>
  <div class="portrait" role="img" aria-label="Portrait of a smiling therapist"></div>
  <p class="welcome-text">Lorem ipsum dolor sit amet, consectetuer adipiscing elit, sed diam nonummy nibh euismod tincidunt ut laoreet dolore magna aliquam erat volutpat. Ut wisi enim ad minim veniam, quis nostrud exerci tation ullamcorper suscipit lobortis nisl ut aliquip ex ea commodo consequat. Duis autem vel eum iriure dolor in hendrerit in vulputate velit esse molestie consequat.</p>
  <p class="welcome-more">Lorem ipsum dolor sit amet, consectetuer adipiscing elit, sed diam nonummy nibh euismod tincidunt ut laoreet dolore magna aliquam erat volutpat. Ut wisi enim ad minim veniam, quis nostrud exerci tation ullamcorper suscipit.</p>
  <div class="slider" role="img" aria-label="Slideshow photo of a parent holding a child's hand">
    <div class="slider-arrows">
      <span><svg width="6" height="8" viewBox="0 0 6 8"><path d="M5 0L1 4l4 4" fill="none" stroke="#333" stroke-width="1.5"/></svg></span>
      <span><svg width="6" height="8" viewBox="0 0 6 8"><path d="M1 0l4 4-4 4" fill="none" stroke="#333" stroke-width="1.5"/></svg></span>
    </div>
  </div>
</section>

<section class="testimonials">
  <h2>WHAT PEOPLE ARE SAYING</h2>
  <div class="title-rule"></div>
  <div class="quotes">
    <div class="quote">
      <div class="avatar" role="img" aria-label="Client portrait"></div>
      <blockquote class="quote-box">“ Lorem ipsum dolor sit amet, consectetuer adipiscing elit, sed diam nonummy nibh euismod tincidunt ut laoreet dolore magna aliquam erat volutpat. ”<cite>People Name</cite></blockquote>
    </div>
    <div class="quote">
      <div class="avatar" role="img" aria-label="Client portrait"></div>
      <blockquote class="quote-box">“ Lorem ipsum dolor sit amet, consectetuer adipiscing elit, sed diam nonummy nibh euismod tincidunt ut laoreet dolore magna aliquam erat volutpat. ”<cite>People Name</cite></blockquote>
    </div>
  </div>
</section>

<footer class="site-footer">
  <div class="footer-col col-contact">
    <h4>CONTACT US</h4>
    <div class="info-row"><svg width="8" height="11" viewBox="0 0 8 11"><path d="M4 0a4 4 0 0 1 4 4c0 3-4 7-4 7S0 7 0 4a4 4 0 0 1 4-4z" fill="#cfcfcf"/><circle cx="4" cy="4" r="1.5" fill="#3a3a3a"/></svg><span><strong>Meadowgate Counselors</strong><br>Lorem ipsum dolor sit amet consectetuer adipiscing elit</span></div>
    <div class="info-row"><svg width="9" height="9" viewBox="0 0 10 10"><path d="M2 0l2 2-1 2c1 1 2 2 3 3l2-1 2 2-2 2C4 10 0 6 0 2z" fill="#cfcfcf"/></svg><span>+123 456 7890</span></div>
    <div class="info-row"><svg width="11" height="8" viewBox="0 0 11 8"><rect x=".5" y=".5" width="10" height="7" fill="none" stroke="#cfcfcf"/><path d="M.5 .5l5 4 5-4" fill="none" stroke="#cfcfcf"/></svg><span>hello@meadowgatecounselors.example</span></div>
  </div>
  <div class="footer-col col-news">
    <h4>NEWSLETTER</h4>
    <p>Sign up to receive our latest news and updates by email today.</p>
    <div class="field">Name</div>
    <div class="field">Email Address</div>
    <span class="btn">SUBSCRIBE</span>
  </div>
  <div class="footer-col col-quick">
    <h4>QUICK CONTACT</h4>
    <div class="field">Name</div>
    <div class="field">Email</div>
    <div class="field tall">Comment</div>
    <span class="btn">SUBMIT</span>
  </div>
</footer>
<div class="footer-bottom">
  <div class="footer-links"><a href="#">Home</a><a href="#">About Us</a><a href="#">Contact Us</a></div>
  <div class="copyright">© Meadowgate Counselors 2015. All Rights Reserved</div>
</div>

</body>
</html>
```